Harborline Stay Collective Business Card Design

Design a business card for Harborline Stay Collective. Look at the website for colors and reference. Card should have logo, name, title, office number, mobile number, email, URL and a tagline like, "Luxury Hotel & Resort Email Marketing" (This might change).

https://www.harborlinestaycollective.net

The rest I will leave up to your imagination.

Contact Information for Business Card

Logo, name, title, office number, mobile number, email, URL and a tagline like, "Luxury Hotel & Resort Email Marketing" (This might change).

```html
<!DOCTYPE html>
<html lang="en">
<head>
<meta charset="utf-8">
<title>Harborline Stay Collective – Business Card</title>
<link rel="stylesheet" href="https://fonts.googleapis.com/css2?family=Open+Sans:wght@400;600;700&display=swap">
<style>
  :root {
    --backdrop: #232323;
    --card: #1f1f22;
    --accent: #f07a22;
    --ink: #ffffff;
    --logo-ink: #3a3a3e;
  }
  * { box-sizing: border-box; margin: 0; padding: 0; }
  html, body {
    width: 1200px; height: 780px; overflow: hidden;
    background: var(--backdrop);
    font-family: "Open Sans", Arial, sans-serif;
  }
  .stage {
    width: 1200px; height: 780px;
    display: flex; align-items: center; justify-content: center; gap: 30px;
  }
  .card {
    position: relative;
    width: 560px; height: 320px;
    background: var(--card);
    border-bottom: 6px solid var(--accent);
    box-shadow: 0 14px 30px rgba(0,0,0,.55);
    overflow: hidden;
  }
  /* Front */
  .card-front { display: flex; align-items: center; justify-content: center; }
  .brand-name {
    color: var(--logo-ink);
    font-weight: 700; font-size: 30px; letter-spacing: .5px;
    text-transform: uppercase;
    text-align: center; line-height: 1.15;
  }
  /* Back */
  .identity {
    position: absolute; left: 36px; top: 146px;
    width: 226px; text-align: right;
  }
  .person-name { font-size: 26px; font-weight: 700; line-height: 1.1; white-space: nowrap; }
  .person-name .first { color: var(--accent); }
  .person-name .last { color: var(--ink); }
  .person-title { color: var(--ink); font-size: 15px; font-weight: 400; margin-top: 2px; white-space: nowrap; }
  .divider {
    position: absolute; left: 282px; top: 100px;
    width: 2px; height: 112px; background: var(--ink);
  }
  .contacts { position: absolute; left: 302px; top: 106px; list-style: none; }
  .contacts li {
    display: flex; align-items: center; gap: 8px;
    color: var(--ink); font-size: 12px; line-height: 25px; white-space: nowrap;
  }
  .contacts svg { width: 13px; height: 13px; flex: none; }
  .tagline {
    position: absolute; left: 0; right: 0; bottom: 40px;
    text-align: center; color: var(--accent); font-size: 16px; padding-left: 60px;
  }
</style>
</head>
<body>
<main class="stage">
  <section class="card card-front" aria-label="Card front">
    <p class="brand-name">Harborline<br>Stay Collective</p>
  </section>

  <section class="card card-back" aria-label="Card back">
    <div class="identity">
      <h1 class="person-name"><span class="first">Marta</span> <span class="last">Kovalenko</span></h1>
      <p class="person-title">Managing Director</p>
    </div>
    <div class="divider"></div>
    <ul class="contacts">
      <li>
        <svg viewBox="0 0 24 24" fill="var(--accent)"><path d="M6.6 10.8a15 15 0 0 0 6.6 6.6l2.2-2.2a1 1 0 0 1 1-.25 11.4 11.4 0 0 0 3.6.57 1 1 0 0 1 1 1V20a1 1 0 0 1-1 1A17 17 0 0 1 3 4a1 1 0 0 1 1-1h3.5a1 1 0 0 1 1 1c0 1.25.2 2.450.57 3.57a1 1 0 0 1-.25 1z"/></svg>
        (555) 214-0386
      </li>
      <li>
        <svg viewBox="0 0 24 24" fill="none" stroke="var(--accent)" stroke-width="2"><rect x="6" y="2" width="12" height="20" rx="2"/><line x1="11" y1="18" x2="13" y2="18"/></svg>
        (555) 214-0719
      </li>
      <li>
        <svg viewBox="0 0 24 24" fill="none" stroke="var(--accent)" stroke-width="2"><circle cx="12" cy="12" r="9"/><path d="M3 12h18M12 3c3 3 3 15 0 18M12 3c-3 3-3 15 0 18"/></svg>
        www.harborlinestaycollective.net
      </li>
      <li>
        <svg viewBox="0 0 24 24" fill="none" stroke="var(--accent)" stroke-width="2"><rect x="3" y="5" width="18" height="14" rx="1"/><path d="M3 6l9 7 9-7"/></svg>
        info@harborlinestaycollective.net
      </li>
    </ul>
    <p class="tagline">Luxury Hotel &amp; Resort Email Marketing</p>
  </section>
</main>
</body>
</html>
```